Brenvick Holdings LLC, new Business cards

I'm moving offices and need new cards. Plus I'm open to modifying the current design of my card. I will keep the logo but would like to explore other layouts and fonts for the design. I've included the current double sided card for reference. I Like the navy color and white. Might be open to grays or silver. Needs to be clean and elegant.

Target Market(s)

Investors, buyers & sellers of private equities and real estate.

Contact Information for Business Card

Brenvick Holdings
Dorian P.K. Halvers, Managing Principal
418 Ostrander Ave., Suite 612
Denver, CO 80319
M: 970-555-0147, O: 303-555-0192
Dorian@brenvickholdings.example
Brenvickholdings.example

Colors
0354a2
ffffff
c4c4c4

Requirements
Must have
• Business card details.
• Logo raised or embossed, it was designed after a wax seal. Current has raised ink.
Nice to have
• Space on card to write additional notes.

```html
<!DOCTYPE html>
<html lang="en">
<head>
<meta charset="utf-8">
<title>Brenvick Holdings – Business Card</title>
<link rel="stylesheet" href="https://fonts.googleapis.com/css2?family=Josefin+Sans:wght@700&family=Lato:wght@400;700&display=swap">
<style>
  :root {
    --backdrop: #efe9e2;
    --kraft-light: #d3ae80;
    --kraft-mid: #c49a6a;
    --kraft-dark: #b58a5a;
    --ink: #1b1612;
    --rule: #6d563e;
    --seal-navy: #24264f;
  }
  * { margin: 0; padding: 0; box-sizing: border-box; }
  html, body {
    width: 1200px;
    height: 900px;
    overflow: hidden;
    background: var(--backdrop);
  }
  .canvas {
    position: relative;
    width: 1200px;
    height: 900px;
  }
  .card {
    position: absolute;
    width: 556px;
    height: 343px;
    background: linear-gradient(160deg, var(--kraft-light) 0%, var(--kraft-mid) 55%, var(--kraft-dark) 100%);
    box-shadow: 3px 4px 6px rgba(0, 0, 0, 0.25);
    color: var(--ink);
    font-family: "Lato", Arial, sans-serif;
    text-align: center;
  }
  .card-front { left: 330px; top: 90px; }
  .card-back { left: 330px; top: 470px; }

  .company-name {
    position: absolute;
    top: 78px;
    left: 0;
    width: 100%;
    font-family: "Josefin Sans", "Helvetica Neue", sans-serif;
    font-weight: 700;
    font-size: 25px;
    letter-spacing: 0.6px;
    text-transform: uppercase;
  }
  .person-name {
    position: absolute;
    top: 168px;
    left: 0;
    width: 100%;
    font-size: 19px;
    letter-spacing: 0.3px;
    text-transform: uppercase;
  }
  .person-title {
    position: absolute;
    top: 191px;
    left: 0;
    width: 100%;
    font-size: 15px;
  }
  .divider {
    position: absolute;
    left: 170px;
    width: 206px;
    height: 1px;
    background: var(--rule);
  }
  .divider-top { top: 222px; }
  .divider-bottom { top: 261px; }
  .address {
    position: absolute;
    top: 232px;
    left: 0;
    width: 100%;
    font-size: 16px;
  }
  .contact-line {
    position: absolute;
    top: 271px;
    left: 0;
    width: 100%;
    font-size: 15px;
    white-space: nowrap;
  }
  .contact-label { font-weight: 700; }
  .website {
    position: absolute;
    top: 295px;
    left: 0;
    width: 100%;
    font-size: 15px;
  }

  .seal-lockup {
    position: absolute;
    left: 0;
    top: 0;
    width: 100%;
    height: 100%;
    display: flex;
    align-items: center;
    justify-content: center;
    gap: 14px;
  }
  .seal-dot {
    width: 48px;
    height: 48px;
    border-radius: 50%;
    background: var(--seal-navy);
  }
  .seal-name {
    font-family: "Josefin Sans", "Helvetica Neue", sans-serif;
    font-weight: 700;
    font-size: 22px;
    letter-spacing: 1.2px;
    text-transform: uppercase;
    color: var(--seal-navy);
  }
</style>
</head>
<body>
  <main class="canvas">
    <section class="card card-front" aria-label="Card front">
      <h1 class="company-name">Brenvick Holdings</h1>
      <p class="person-name">Dorian P.K. Halvers</p>
      <p class="person-title">Managing Principal</p>
      <div class="divider divider-top"></div>
      <p class="address">418 Ostrander Ave., Suite 612 Denver, CO 80319</p>
      <div class="divider divider-bottom"></div>
      <p class="contact-line">M: 970-555-0147&nbsp; | <span class="contact-label">O:</span> 303-555-0192 | Dorian@brenvickholdings.example</p>
      <p class="website">Brenvickholdings.example</p>
    </section>

    <section class="card card-back" aria-label="Card back">
      <div class="seal-lockup">
        <span class="seal-dot"></span>
        <span class="seal-name">Brenvick Holdings</span>
      </div>
    </section>
  </main>
</body>
</html>
```